Velora Aesthetica

Medical doctor providing aesthetic medicine

* Double sided card
* Logo to be on card
Other details:
* Dr. Mirela Kostvan, BSc, MBChB, CCFP
* #214-215, 27903 83 Ave, Surrey, BC, V2T 4K7
* 604-718-2943
* info@veloraclinic.ca
* www.veloraclinic.ca

Industry/Entity Type

Medical / Health & Beauty

Contact Information for Business Card

see 'Project Description'

Colors
0054AA
0677BA
7BADD7
CADEEF
E8F1F8
FFF300
FFF600
FEFA6F
FFFEC7
FFFEE8

Requirements
Must have
• Modern, high-end design

```html
<!DOCTYPE html>
<html lang="en">
<head>
<meta charset="UTF-8">
<title>Velora Aesthetica – Business Card</title>
<link rel="stylesheet" href="https://fonts.googleapis.com/css2?family=Montserrat:wght@400;500;600&display=swap">
<style>
  :root {
    --backdrop: #717171;
    --navy: #22405f;
    --navy-text: #1f3a5c;
    --gold: #d0a92c;
    --ink: #111111;
    --grey-text: #5f5f5f;
    --paper: #ffffff;
  }
  * { box-sizing: border-box; margin: 0; padding: 0; }
  html, body {
    width: 1200px; height: 1000px; overflow: hidden;
    background: var(--backdrop);
    font-family: "Montserrat", sans-serif;
  }
  .stage {
    width: 1200px; height: 1000px;
    display: flex; flex-direction: column; align-items: center; justify-content: center;
    gap: 60px;
  }
  .card {
    width: 612px; height: 352px;
    border-radius: 22px;
    position: relative;
    overflow: hidden;
  }
  /* Front */
  .card-front {
    background: var(--navy);
    display: flex; align-items: center; justify-content: center;
  }
  .front-name {
    color: var(--gold);
    font-weight: 500;
    font-size: 34px;
    letter-spacing: 0.22em;
    text-transform: uppercase;
    text-align: center;
    line-height: 1.3;
  }
  /* Back */
  .card-back {
    background: var(--paper);
    display: flex; align-items: center;
  }
  .brand-block {
    width: 340px;
    display: flex; flex-direction: column; align-items: center; gap: 18px;
  }
  .brand-dot {
    width: 84px; height: 84px;
    border-radius: 50%;
    border: 3px solid var(--gold);
  }
  .brand-name {
    color: var(--ink);
    font-weight: 500;
    font-size: 24px;
    letter-spacing: 0.16em;
    text-transform: uppercase;
    text-align: center;
    line-height: 1.3;
  }
  .contact-block {
    width: 200px;
    margin-left: 8px;
    text-align: center;
    display: flex; flex-direction: column; align-items: center;
  }
  .person-name { color: var(--navy-text); font-weight: 600; font-size: 17px; }
  .person-credentials { color: var(--navy-text); font-weight: 500; font-size: 14px; margin-top: 3px; }
  .contact-icons { display: flex; gap: 6px; margin: 12px 0 8px; }
  .contact-icon {
    width: 24px; height: 24px; border-radius: 50%;
    background: var(--gold);
    display: flex; align-items: center; justify-content: center;
  }
  .contact-line { color: var(--grey-text); font-size: 13.5px; line-height: 1.3; }
  .divider { width: 86px; height: 3px; background: var(--gold); margin: 12px 0 10px; }
  .address { color: var(--grey-text); font-size: 13.5px; line-height: 1.3; }
</style>
</head>
<body>
  <main class="stage">
    <section class="card card-front" aria-label="Card front">
      <p class="front-name">Velora Aesthetica</p>
    </section>

    <section class="card card-back" aria-label="Card back">
      <div class="brand-block">
        <span class="brand-dot" aria-hidden="true"></span>
        <p class="brand-name">Velora Aesthetica</p>
      </div>
      <div class="contact-block">
        <p class="person-name">Dr. Mirela Kostvan</p>
        <p class="person-credentials">BSc, MBChB, CCFP</p>
        <div class="contact-icons" aria-hidden="true">
          <span class="contact-icon">
            <svg width="13" height="13" viewBox="0 0 24 24"><path fill="#fff" d="M6.6 10.8a15.2 15.2 0 0 0 6.6 6.6l2.2-2.2c.3-.3.7-.4 1-.2 1.1.4 2.3.6 3.6.6.6 0 1 .4 1 1V20c0 .6-.4 1-1 1A17 17 0 0 1 3 4c0-.6.4-1 1-1h3.5c.6 0 1 .4 1 1 0 1.3.2 2.5.6 3.6.1.3 0 .7-.2 1z"/></svg>
          </span>
          <span class="contact-icon">
            <svg width="13" height="13" viewBox="0 0 24 24"><rect x="3" y="6" width="18" height="12" rx="1" fill="#fff"/><path d="M3.5 6.5 12 13l8.5-6.5" fill="none" stroke="#d0a92c" stroke-width="1.6"/></svg>
          </span>
          <span class="contact-icon">
            <svg width="13" height="13" viewBox="0 0 24 24" fill="none" stroke="#fff" stroke-width="1.8"><circle cx="12" cy="12" r="9"/><ellipse cx="12" cy="12" rx="4" ry="9"/><path d="M3 12h18M5 7h14M5 17h14"/></svg>
          </span>
        </div>
        <p class="contact-line">(604) 718 2943</p>
        <p class="contact-line">info@veloraclinic.ca</p>
        <p class="contact-line">www.veloraclinic.ca</p>
        <span class="divider" aria-hidden="true"></span>
        <p class="address">#214-215, 27903 83 Ave,<br>Surrey, BC, V2T 4K7</p>
      </div>
    </section>
  </main>
</body>
</html>
```